Webdesign Chiropraktik
Zielgruppe
Amerikanische Chiropraktik
Aufgabenstellung
keine direkten vorgaben...Wir sind ein junges Team und brauchen eine moderne ansprechende Webseite...

```html
<!DOCTYPE html>
<html lang="de">
<head>
<meta charset="utf-8">
<title>Chiropraxis Wendlinger</title>
<link href="https://fonts.googleapis.com/css2?family=Poppins:wght@300;400;500;600;700&display=swap" rel="stylesheet">
<style>
:root{
  --green:#6a9e2a;
  --green-dark:#5a8a22;
  --ink:#333;
  --muted:#666;
  --pale:#e9eff9;
  --footer:#efefef;
  --footer-bar:#555;
  --white:#fff;
}
*{margin:0;padding:0;box-sizing:border-box}
html,body{width:1200px;height:4899px;overflow:hidden}
body{position:relative;font-family:"Poppins",sans-serif;color:var(--ink);background:var(--white);font-weight:300}
.abs{position:absolute}
.photo{position:absolute}
h2.section-title{font-family:"Poppins",sans-serif;font-weight:700;color:var(--green);font-size:36px;line-height:1.1;letter-spacing:-.5px}
.subtitle{font-weight:600;font-size:14px;color:var(--ink);margin-top:4px}
.body-text{font-size:13px;line-height:25px;color:var(--ink)}
.body-text p+p{margin-top:18px}

.header{top:0;left:0;width:1200px;height:160px;background:var(--white)}
.header .phone{left:356px;top:33px;font-size:11px;color:var(--green);display:flex;gap:6px;align-items:center}
.brand{left:500px;top:28px;width:200px;text-align:center;font-size:17px;font-weight:600;color:var(--green);display:flex;flex-direction:column;align-items:center;gap:8px}
.brand .dot{width:44px;height:44px;border-radius:50%;background:var(--green)}
.social{left:724px;top:35px;display:flex;gap:10px}
.social span{width:13px;height:13px;border-radius:50%;background:var(--green)}
.legal{left:895px;top:36px;font-size:9px;color:#888;display:flex;gap:8px}
.nav{top:117px;font-size:12px;letter-spacing:1.2px;color:#666;display:flex;gap:26px;font-weight:400}
.nav .active{color:var(--green)}

.hero{top:160px;left:0;width:1200px;height:495px;background:linear-gradient(100deg,#5a4f49 0%,#8a7a70 35%,#3d3b3a 65%,#2a2a2a 100%)}
.hero-title{left:196px;top:245px;color:#4a4a4a;font-weight:700;font-size:40px;line-height:36px;letter-spacing:-.5px}
.hero-sub{left:196px;top:322px;color:#fff;font-size:17px;line-height:21px;font-weight:300}
.arrow{top:380px;width:44px;height:44px;background:rgba(120,120,120,.75);border:1px solid rgba(255,255,255,.6);display:flex;align-items:center;justify-content:center}
.band{top:655px;left:0;width:1200px;height:18px;background:var(--pale)}

.intro-text{left:178px;top:768px;width:470px}
.intro-text .body-text{margin-top:30px;font-size:12.5px;line-height:22.5px}

.services{top:1340px;left:0;width:1200px;height:740px;background:var(--pale)}
.services-head{left:0;top:1412px;width:1200px;text-align:center}
.vline{left:600px;top:1535px;height:450px;border-left:2px dotted #777}
.hline{left:218px;top:1770px;width:762px;border-top:2px dotted #777}
.center-dot{left:594px;top:1765px;width:12px;height:12px;border-radius:50%;background:#555}
.service{width:300px;text-align:center}
.service svg{display:block;margin:0 auto}
.service h3{color:var(--green);font-weight:600;font-size:17px;margin-top:14px}
.service p{font-size:13px;line-height:20px;color:var(--ink);margin-top:6px}

.goal-text{left:600px;top:2160px;width:400px}
.goal-text .body-text{margin-top:18px;font-size:12.8px}
.btn{display:inline-block;margin-top:26px;background:var(--green);color:#fff;font-size:12px;font-weight:600;padding:9px 44px;box-shadow:0 2px 0 var(--green-dark)}

.team{top:2717px;left:0;width:1200px;height:1048px;background:var(--pale)}
.member-panel{left:460px;width:740px;height:238px;background:var(--white)}
.member-info{left:490px}
.member-info h3{color:var(--green);font-weight:700;font-size:22px}
.member-info .role{font-size:13px;color:#444;margin-top:2px}
.acc{width:403px;height:38px;background:var(--pale);margin-top:17px;display:flex;align-items:center;justify-content:space-between;padding:0 14px;font-size:13px;font-weight:600}
.acc + .acc{margin-top:17px}

.contact-text{left:630px;top:3865px;width:400px}
.contact-text .body-text{font-size:13px}

.hours{left:178px;top:4318px}
.hours table{margin-top:24px;border-collapse:collapse;font-size:16px;color:#333}
.hours td{padding:2px 0;line-height:24px}
.hours td:first-child{width:124px}

.footer{top:4582px;left:0;width:1200px;height:258px;background:var(--footer)}
.footer h4{font-weight:600;font-size:18px;color:#333}
.footer .body-text{font-size:14px;line-height:25px;margin-top:24px;color:#444}
.footer-bar{top:4840px;left:0;width:1200px;height:59px;background:var(--footer-bar);color:#eee;font-size:12px;padding:22px 0 0 178px}
</style>
</head>
<body>

<header class="abs header">
  <div class="abs phone">
    <svg width="11" height="11" viewBox="0 0 24 24"><path fill="#6a9e2a" d="M6.6 10.8a15 15 0 0 0 6.6 6.6l2.2-2.2c.3-.3.7-.4 1-.2 1.1.4 2.3.6 3.6.6.6 0 1 .4 1 1V20c0 .6-.4 1-1 1C10.6 21 3 13.4 3 4c0-.6.4-1 1-1h3.5c.6 0 1 .4 1 1 0 1.3.2 2.5.6 3.6.1.3 0 .7-.2 1z"/></svg>
    08122 5550147
  </div>
  <div class="abs brand"><span class="dot"></span>Wendlinger</div>
  <div class="abs social"><span></span><span></span><span></span></div>
  <div class="abs legal"><span>Datenschutz</span><span>Impressum</span></div>
  <nav class="abs nav" style="left:183px"><span class="active">HOME</span><span>LEISTUNGEN</span><span>ZIELSETZUNG</span></nav>
  <nav class="abs nav" style="left:723px"><span>TEAM</span><span>KONTAKT</span><span>ÖFFNUNGSZEITEN</span></nav>
</header>

<section>
  <div class="photo hero" role="img" aria-label="Chiropraktiker behandelt den Nacken einer liegenden Patientin"></div>
  <div class="abs hero-title">Amerikanische<br>Chiropraktik</div>
  <div class="abs hero-sub">Ein Ansatz, der den Menschen<br>ganzheitlich wahrnimmt</div>
  <div class="abs arrow" style="left:20px"><svg width="16" height="26" viewBox="0 0 16 26"><path d="M13 2 3 13l10 11" stroke="#fff" stroke-width="2" fill="none"/></svg></div>
  <div class="abs arrow" style="left:1136px"><svg width="16" height="26" viewBox="0 0 16 26"><path d="M3 2l10 11L3 24" stroke="#fff" stroke-width="2" fill="none"/></svg></div>
  <div class="abs band"></div>
</section>

<section>
  <div class="abs intro-text">
    <h2 class="section-title">Chiropraktik in Falkenau</h2>
    <div class="subtitle">Amerikanische Chiropraktik nun auch in Falkenau!</div>
    <div class="body-text">
      <p>Die Chiropraktik beschäftigt sich primär mit den Störungen des Nervensystems im Körper. Gibt es in unserem Hauptorgan (Gehirn) einen Fehler/Schwäche kann sich das in unserem Körper spiegeln! Meistens reagiert der Körper mit einer lokalen Verspannung eines Muskels. Daraus kann eine Einschränkung der Gelenkbeweglichkeit resultieren.</p>
      <p>Der Chiropraktiker muss also mittels neurologischen Tests herausfinden, wo sich der Fehler im Gehirn befindet. Durch gezielte Justierungen an der Wirbelsäule und an peripheren Gelenken kann der Chiropraktiker das Gehirn positiv beeinflussen. Je weniger Fehler im Gehirn, desto besser die Funktion des Körpers -&gt; WENIGER Symptome!</p>
      <p>Wird das Gehirn, wie bei allen Aktivitäten, regelmäßig positiv stimuliert, gibt es sowohl im Gehirn als auch im Körper positive Veränderungen. Heilung ist also ein Prozess und kein Event.</p>
    </div>
  </div>
  <div class="photo" style="left:700px;top:765px;width:500px;height:485px;background:linear-gradient(160deg,#c98e6c 0%,#8a6a5c 45%,#2f3650 75%,#1f2740 100%)" role="img" aria-label="Justierinstrument setzt einen Impuls am Rücken"></div>
</section>

<section>
  <div class="abs services"></div>
  <div class="abs services-head">
    <h2 class="section-title">Leistungen</h2>
    <div class="subtitle">Von der Anamnese bis zur Justierung</div>
  </div>
  <div class="abs vline"></div>
  <div class="abs hline"></div>
  <div class="abs center-dot"></div>

  <div class="abs service" style="left:230px;top:1540px">
    <svg width="96" height="90" viewBox="0 0 96 90" fill="none" stroke="#222" stroke-width="2"><rect x="50" y="10" width="36" height="24" rx="3"/><path d="M56 18h24M56 25h16"/><path d="M20 10c-10 4-12 16-8 26l-4 8h6v10h10v12"/><circle cx="70" cy="70" r="11"/><path d="M70 64v12M64 70h12"/></svg>
    <h3>Das Anamnesegespräch</h3>
    <p>Ausführliche Erfragung bezüglich Ihrer<br>Hauptprobleme.</p>
  </div>
  <div class="abs service" style="left:652px;top:1535px">
    <svg width="96" height="95" viewBox="0 0 96 95" fill="none" stroke="#222" stroke-width="2"><circle cx="48" cy="30" r="24"/><circle cx="48" cy="26" r="8"/><path d="M48 34v50M48 60c-10-8-20-6-24 0M48 60c10-8 20-6 24 0M24 84h48"/></svg>
    <h3>Die Untersuchung</h3>
    <p>Untersuchung des ganzen Körpers<br>in Statik und aktiver Beweglichkeit.</p>
  </div>
  <div class="abs service" style="left:230px;top:1805px">
    <svg width="96" height="90" viewBox="0 0 96 90" fill="none" stroke="#222" stroke-width="2"><circle cx="44" cy="30" r="24"/><circle cx="44" cy="30" r="17"/><path d="M32 30c6-8 18-8 24 0-6 8-18 8-24 0z"/><circle cx="44" cy="30" r="3"/><path d="M44 54v12M36 66h20v18H36zM56 70h10"/></svg>
    <h3>Neurologische Testungen</h3>
    <p>Herausfinden mögliche Fehler des<br>Nervensystems.</p>
  </div>
  <div class="abs service" style="left:652px;top:1805px">
    <svg width="96" height="90" viewBox="0 0 96 90" fill="none" stroke="#222" stroke-width="2"><path d="M58 10c-4-6-12 0-6 6l6 5 6-5c6-6-2-12-6-6z"/><path d="M30 40c-3-5-10 0-5 5l5 4 5-4c5-5-2-10-5-5z"/><path d="M40 50h8l6-18c4-2 8 2 6 8l-2 10h14v26H40z"/><path d="M28 50h12v28H28zM46 8v10M80 30h8M74 82v8M70 86h8"/></svg>
    <h3>Körperjustierung</h3>
    <p>Sanfte Impulse an Wirbelsäule und<br>peripheren Gelenken beheben Fehler.</p>
  </div>
</section>

<section>
  <div class="photo" style="left:0;top:2080px;width:540px;height:637px;background:linear-gradient(135deg,#e6e2dc 0%,#bfa89a 40%,#4a3a34 70%,#2a2a2e 100%)" role="img" aria-label="Chiropraktiker justiert die Schulter einer Patientin auf der Behandlungsliege"></div>
  <div class="abs goal-text">
    <h2 class="section-title">Zielsetzung</h2>
    <div class="subtitle">Heilung Ihrer Beschwerden</div>
    <div class="body-text">
      <p>Das Ziel der amerikanische Chiropraktik behebt Fehler in Wirbelsäule und Gelenken und regt das Nervensystem positiv an. Folglich schwinden Symptome automatisch. Der Ersttermin umfasst ein ausführliches Anamnesegespräch, eine körperliche Untersuchung und die anschließende Behandlung (Justierung). Nach dieser Sitzung wird ein individueller Behandlungsplan für Sie erstellt.</p>
      <p>Laden Sie bereits vor ihrem Termin unseren Anamnesebogen auf ihren Rechner , sie können Ihn bequem zuhause ausfüllen und zum ersten Termin mitbringen.</p>
    </div>
    <span class="btn">Anamnesebogen</span>
  </div>
</section>

<section>
  <div class="abs team"></div>
  <h2 class="abs section-title" style="left:178px;top:2805px">Unsere Team</h2>

  <div class="photo" style="left:178px;top:2892px;width:265px;height:238px;background:linear-gradient(160deg,#5f7a48 0%,#d9d4cc 50%,#222 100%)" role="img" aria-label="Porträt des Chiropraktikers mit Wirbelsäulenmodell"></div>
  <div class="abs member-panel" style="top:2892px"></div>
  <div class="abs member-info" style="top:2925px">
    <h3>Malte Wendlinger</h3>
    <div class="role">Chiropraktiker, Heilpraktiker und Physiotherapeut</div>
    <div class="acc">Fachkenntnisse<svg width="8" height="12" viewBox="0 0 8 12"><path d="M1 1l5 5-5 5" stroke="#6a9e2a" stroke-width="2" fill="none"/></svg></div>
    <div class="acc">Schulische u. medizinische Ausbildung<svg width="8" height="12" viewBox="0 0 8 12"><path d="M1 1l5 5-5 5" stroke="#6a9e2a" stroke-width="2" fill="none"/></svg></div>
  </div>

  <div class="photo" style="left:178px;top:3164px;width:265px;height:238px;background:linear-gradient(160deg,#eeeeee 0%,#c9c9c9 45%,#3bb7a0 80%,#2e9c88 100%)" role="img" aria-label="Porträt des Heilpraktikers im türkisen Shirt"></div>
  <div class="abs member-panel" style="top:3164px"></div>
  <div class="abs member-info" style="top:3197px">
    <h3>Jonas Reffke</h3>
    <div class="role">Heilpraktiker / Chiropraktiker</div>
    <div class="acc">Fachkenntnisse<svg width="8" height="12" viewBox="0 0 8 12"><path d="M1 1l5 5-5 5" stroke="#6a9e2a" stroke-width="2" fill="none"/></svg></div>
    <div class="acc">Schulische u. medizinische Ausbildung<svg width="8" height="12" viewBox="0 0 8 12"><path d="M1 1l5 5-5 5" stroke="#6a9e2a" stroke-width="2" fill="none"/></svg></div>
  </div>

  <div class="photo" style="left:178px;top:3437px;width:265px;height:238px;background:linear-gradient(170deg,#f0f0f0 0%,#d8d4d0 50%,#e8c6c0 100%)" role="img" aria-label="Porträt der chiropraktischen Assistentin"></div>
  <div class="abs member-panel" style="top:3437px"></div>
  <div class="abs member-info" style="top:3470px">
    <h3>Larissa</h3>
    <div class="role">Chiropraktische Assistenz / Praxismanagement</div>
  </div>
</section>

<section>
  <div class="photo" style="left:0;top:3765px;width:578px;height:520px;background:linear-gradient(150deg,#f2f2f2 0%,#dcdcdc 50%,#9a8a78 100%)" role="img" aria-label="Heller Praxisraum mit Schreibtisch und Bildern an der Wand"></div>
  <div class="abs contact-text">
    <h2 class="section-title">Kontakt</h2>
    <div class="body-text" style="margin-top:20px">
      <p>Lernen Sie uns in unserer Praxis in Altfalkenau kennen! Große helle Räume, modernstes Equipment und eine Atmosphäre zum Entspannen und Wohlfühlen.</p>
      <p>Lindenhofstrasse 14<br>85399 Falkenau</p>
    </div>
    <svg style="margin-top:12px" width="58" height="40" viewBox="0 0 58 40" fill="none" stroke="#222" stroke-width="2"><rect x="2" y="4" width="50" height="30"/><path d="M2 4l25 18L52 4"/><circle cx="30" cy="32" r="6" fill="#fff"/><path d="M30 29v6M27 32h6"/></svg>
    <div class="body-text" style="margin-top:10px"><b style="font-weight:600">Tel:</b> 08122 5550147<br><b style="font-weight:600">E-Mail:</b> info@chiropraktik-falkenau.de</div>
  </div>
</section>

<section>
  <div class="abs hours">
    <h2 class="section-title">Öffnungszeiten</h2>
    <table>
      <tr><td>Montag</td><td>13:00-20:00 Uhr</td></tr>
      <tr><td>Dienstag</td><td>10:00-17:00 Uhr</td></tr>
      <tr><td>Mittwoch</td><td>13:00-20:00 Uhr</td></tr>
      <tr><td>Donnerstag</td><td>08:00-15:00 Uhr</td></tr>
      <tr><td>Freitag</td><td>geschlossen</td></tr>
    </table>
  </div>
  <div class="photo" style="left:578px;top:4285px;width:622px;height:297px;background:linear-gradient(120deg,#c9a274 0%,#6d5a48 40%,#3a3030 70%,#8a8580 100%)" role="img" aria-label="Behandlungsraum mit mehreren Chiropraktik-Liegen"></div>
</section>

<footer>
  <div class="abs footer"></div>
  <div class="abs" style="left:178px;top:4628px;width:300px">
    <h4>Über uns</h4>
    <div class="body-text">Lernen Sie mich in meiner Praxis<br>in Altfalkenau kennen! Große helle<br>Räume, modernstes Equipment und<br>eine Atmosphäre zum Entspannen<br>und Wohlfühlen.</div>
  </div>
  <div class="abs" style="left:534px;top:4628px;width:300px">
    <h4>Adresse</h4>
    <div class="body-text">Lindenhofstrasse 14<br>85399 Falkenau<br>08122 5550147<br>info@chiropraktik-falkenau.de</div>
  </div>
  <div class="abs footer-bar">© 2022 Chiropraxis Wendlinger. Alle Rechte vorbehalten.</div>
</footer>

</body>
</html>
```